Heronby Mortgage Capital Business Card

We need a business card design for our mortgage servicing company. In addition to servicing the loans of homeowners, we help homeowners with purchasing their homes and any mortgage refinancing. We would like to see designs that use the colors in the logo attached below (gold-ish yellow and navy blue), and any other design you deem fit! The design should communicate a simpler life with smart mortgages provided by Heronby.

```html
<!DOCTYPE html>
<html lang="en">
<head>
<meta charset="utf-8">
<title>Heronby Mortgage Capital Business Card</title>
<link rel="stylesheet" href="https://fonts.googleapis.com/css2?family=EB+Garamond:wght@600;700&family=Montserrat:wght@400;500&display=swap">
<style>
  :root {
    --backdrop: #d2d3d5;
    --card: #ffffff;
    --gold: #dcae3c;
    --navy: #1c1a55;
    --ink: #2a2a44;
  }
  * { margin: 0; padding: 0; box-sizing: border-box; }
  html, body {
    width: 900px;
    height: 1200px;
    overflow: hidden;
    background: var(--backdrop);
  }
  .canvas {
    position: relative;
    width: 900px;
    height: 1200px;
  }
  .card {
    position: absolute;
    left: 135px;
    width: 630px;
    height: 360px;
    background: var(--card);
  }
  .card--front { top: 213px; }
  .card--back { top: 627px; }

  .wordmark {
    position: absolute;
    font-family: "EB Garamond", Georgia, serif;
    font-weight: 700;
    color: var(--gold);
    white-space: nowrap;
    line-height: 1;
    transform: translate(-50%, -50%);
  }
  .card--front .wordmark { left: 315px; top: 181px; font-size: 54px; }
  .card--back .wordmark { left: 456px; top: 82px; font-size: 40px; }

  .accent-bar {
    position: absolute;
    left: 0;
    top: 151px;
    width: 12px;
    height: 44px;
    background: var(--navy);
  }
  .person-name {
    position: absolute;
    left: 37px;
    top: 148px;
    font-family: "EB Garamond", Georgia, serif;
    font-weight: 600;
    font-size: 24px;
    color: var(--gold);
    line-height: 1;
  }
  .person-title {
    position: absolute;
    left: 37px;
    top: 178px;
    font-family: "Montserrat", Arial, sans-serif;
    font-size: 14px;
    letter-spacing: 0.6px;
    color: var(--ink);
  }
  .address {
    position: absolute;
    left: 378px;
    top: 200px;
    font-family: "Montserrat", Arial, sans-serif;
    font-size: 14px;
    line-height: 22px;
    letter-spacing: 0.4px;
    color: var(--ink);
    font-style: normal;
  }
  .contact-list {
    position: absolute;
    left: 378px;
    top: 254px;
    list-style: none;
    font-family: "Montserrat", Arial, sans-serif;
    font-size: 14px;
    letter-spacing: 0.6px;
    color: var(--ink);
  }
  .contact-list li {
    display: flex;
    align-items: center;
    height: 24px;
  }
  .contact-list .phone { letter-spacing: 2px; }
  .contact-icon {
    width: 11px;
    height: 11px;
    margin-right: 7px;
    flex: none;
  }
</style>
</head>
<body>
<main class="canvas">
  <section class="card card--front">
    <div class="wordmark">Heronby Mortgage</div>
  </section>

  <section class="card card--back">
    <div class="wordmark">Heronby Mortgage</div>

    <div class="accent-bar"></div>
    <h1 class="person-name">Dana Whitcombe</h1>
    <p class="person-title">Founder</p>

    <address class="address">418 Harbor Lane S<br>Bayview, FL 33012</address>

    <ul class="contact-list">
      <li class="phone">
        <svg class="contact-icon" viewBox="0 0 12 12"><path fill="#dcae3c" d="M2.4 0.6l2 2.2-1 1.4c.7 1.6 1.8 2.7 3.4 3.4l1.4-1 2.2 2-1.1 2c-4.5-.4-8.3-4.2-8.7-8.7z"/></svg>
        (888)-555-0142
      </li>
      <li>
        <svg class="contact-icon" viewBox="0 0 12 12"><rect x="0.5" y="2" width="11" height="8" fill="#dcae3c"/><path d="M0.8 2.4L6 6.6l5.2-4.2" fill="none" stroke="#fff" stroke-width="1"/></svg>
        info@heronbymtg.com
      </li>
      <li>
        <svg class="contact-icon" viewBox="0 0 12 12"><g fill="none" stroke="#dcae3c" stroke-width="1.1"><circle cx="6" cy="6" r="5"/><ellipse cx="6" cy="6" rx="2.2" ry="5"/><path d="M1 6h10M2 3.3h8M2 8.7h8"/></g></svg>
        www.heronbymtg.com
      </li>
    </ul>
  </section>
</main>
</body>
</html>
```